Harborline Stay Collective Business Card Design

Design a business card for Harborline Stay Collective. Look at the website for colors and reference. Card should have logo, name, title, office number, mobile number, email, URL and a tagline like, "Luxury Hotel & Resort Email Marketing" (This might change).

https://www.harborlinestaycollective.net

The rest I will leave up to your imagination.

Contact Information for Business Card

Logo, name, title, office number, mobile number, email, URL and a tagline like, "Luxury Hotel & Resort Email Marketing" (This might change).

```html
<!DOCTYPE html>
<html lang="en">
<head>
<meta charset="UTF-8">
<title>Harborline Stay Collective Business Card</title>
<link href="https://fonts.googleapis.com/css2?family=Montserrat:wght@400;500;700;800&display=swap" rel="stylesheet">
<style>
  :root {
    --backdrop: #b0b1b0;
    --brand-orange: #f37521;
    --card-white: #ffffff;
    --ink: #1d1d1d;
    --ghost: #f5f5f5;
  }
  * { margin: 0; padding: 0; box-sizing: border-box; }
  html, body {
    width: 1200px; height: 900px; overflow: hidden;
    background: var(--backdrop);
    font-family: "Montserrat", sans-serif;
  }
  .stage {
    position: relative; width: 1200px; height: 900px;
    display: flex; flex-direction: column; align-items: center; justify-content: center;
    gap: 44px;
  }
  .card {
    position: relative; width: 640px; height: 366px; overflow: hidden;
  }
  .card--front {
    background: var(--brand-orange);
    border-radius: 22px;
    display: flex; flex-direction: column; align-items: center; justify-content: center;
    color: var(--card-white);
    padding: 0 48px;
  }
  .brand-lockup {
    display: flex; align-items: center; gap: 14px;
    margin-top: -30px;
    max-width: 100%;
  }
  .brand-mark {
    width: 18px; height: 18px; background: var(--card-white); flex-shrink: 0;
  }
  .brand-name {
    font-weight: 800; font-size: 25px; letter-spacing: 0.5px; text-transform: uppercase;
    line-height: 1; white-space: nowrap;
  }
  .tagline {
    position: absolute; bottom: 56px; left: 0; right: 0; text-align: center;
    font-weight: 700; font-size: 13px; letter-spacing: 0.3px;
  }
  .card--back {
    background: var(--card-white);
    border-left: 2px solid var(--brand-orange);
    border-bottom: 2px solid var(--brand-orange);
  }
  .ghost-name {
    position: absolute; left: 50%; top: 50%; transform: translate(-50%, -50%);
    font-weight: 800; font-size: 72px; color: var(--ghost); letter-spacing: 2px;
    white-space: nowrap; text-transform: uppercase;
  }
  .contact-block {
    position: absolute; left: 50%; top: 50%; transform: translate(-50%, -50%);
    display: flex; align-items: stretch;
  }
  .person {
    display: flex; flex-direction: column; align-items: flex-end; justify-content: center;
    padding-right: 18px;
  }
  .person__name { font-weight: 700; font-size: 24px; color: var(--brand-orange); line-height: 1.1; white-space: nowrap; }
  .person__title { font-weight: 400; font-size: 14px; color: var(--ink); }
  .divider { width: 2px; background: var(--brand-orange); }
  .details { list-style: none; padding-left: 16px; }
  .details li {
    display: flex; align-items: center; gap: 10px;
    font-size: 13px; color: var(--ink); line-height: 22px; white-space: nowrap;
  }
  .details svg { width: 13px; height: 13px; fill: var(--brand-orange); flex-shrink: 0; }
</style>
</head>
<body>
<main class="stage">
  <section class="card card--front" aria-label="Card front">
    <div class="brand-lockup">
      <span class="brand-mark"></span>
      <span class="brand-name">Harborline Stay Collective</span>
    </div>
    <p class="tagline">Luxury Hotel &amp; Resort Email Marketing</p>
  </section>

  <section class="card card--back" aria-label="Card back">
    <span class="ghost-name" aria-hidden="true">Harborline</span>
    <div class="contact-block">
      <div class="person">
        <span class="person__name">Jonah Whitcombe</span>
        <span class="person__title">Owner</span>
      </div>
      <span class="divider"></span>
      <ul class="details">
        <li>
          <svg viewBox="0 0 16 16"><path d="M2 6c0-2 2-3 6-3s6 1 6 3v1h-3V5.5C10 5 9 5 8 5S6 5 5 5.5V7H2zM4 8h8l1 5H3z"/></svg>
          555.210.4830 x 204
        </li>
        <li>
          <svg viewBox="0 0 16 16"><path d="M4 1h8v14H4zM5.5 2.5v9h5v-9zM7 12.5h2v1H7z"/></svg>
          555.390.7712
        </li>
        <li>
          <svg viewBox="0 0 16 16"><path d="M1 3h14v10H1zM2.5 4.5 8 9l5.5-4.5z"/></svg>
          info@harborlinestaycollective.net
        </li>
        <li>
          <svg viewBox="0 0 16 16"><path d="M8 1a7 7 0 1 0 0 14A7 7 0 0 0 8 1zm0 2c.8 1 1.3 2.4 1.4 4H6.6C6.7 5.4 7.2 4 8 3zM3.1 9h2.5c.1 1.4.5 2.7 1.1 3.7A5 5 0 0 1 3.1 9zm0-2a5 5 0 0 1 3.6-3.7C6.1 4.3 5.7 5.6 5.6 7zm6.2 5.7c.6-1 1-2.3 1.1-3.7h2.5a5 5 0 0 1-3.6 3.7zM10.4 7c-.1-1.4-.5-2.7-1.1-3.7A5 5 0 0 1 12.9 7z"/></svg>
          www.harborlinestaycollective.net
        </li>
      </ul>
    </div>
  </section>
</main>
</body>
</html>
```